Whitmore Business Card Design

The name of the business is Dara Whitmore, CPA LLC
The service that we offer is Accounting, Tax & Consulting Services. I need it to have the following items:
Dara Whitmore, Principal
Phone Number
Email Address
Physical Address

I have attached the company logo, one in black and one in white. Please provide a design in black background and the other in white background. Please include "Accounting, Tax & Consulting Services". I want the business card to be clean and very professional.

```html
<!DOCTYPE html>
<html lang="en">
<head>
<meta charset="utf-8">
<title>Dara Whitmore, CPA LLC — Business Card</title>
<link rel="stylesheet" href="https://fonts.googleapis.com/css2?family=Montserrat:wght@500;600&family=Arimo:wght@400&display=swap">
<style>
  :root{
    --page:#ececec;
    --card:#3a3b3d;
    --white:#f2f2f2;
    --silver:#8d8e90;
    --red:#8e1a1c;
    --rule:#9a9a9a;
  }
  *{margin:0;padding:0;box-sizing:border-box}
  html,body{width:1200px;height:802px;overflow:hidden;background:var(--page)}
  .stage{width:1200px;height:802px;display:flex;align-items:center;justify-content:center;gap:50px}
  .card{position:relative;width:540px;height:309px;background:var(--card);color:var(--white);
    box-shadow:0 6px 18px rgba(0,0,0,.18);font-family:"Arimo",Arial,sans-serif}

  /* front */
  .front .brand{position:absolute;top:42px;left:0;right:0;text-align:center}
  .brand-row{display:inline-flex;align-items:center;gap:10px}
  .brand-square{width:16px;height:16px;background:var(--white)}
  .brand-name{font-family:"Montserrat",Arial,sans-serif;font-weight:600;font-size:21px;letter-spacing:.5px;color:var(--white);text-transform:uppercase}
  .brand-tagline{font-family:"Montserrat",Arial,sans-serif;font-weight:600;font-size:12.5px;letter-spacing:2.2px;color:var(--silver);text-transform:uppercase;margin-top:4px}
  .details{position:absolute;top:148px;left:0;right:0;display:flex;justify-content:center;align-items:center;gap:22px}
  .person{text-align:right}
  .person-name{font-family:"Montserrat",Arial,sans-serif;font-weight:500;font-size:21px;color:var(--red);text-transform:uppercase;letter-spacing:.5px}
  .person-title{font-size:15px;color:var(--white);margin-top:6px}
  .divider{width:1px;height:72px;background:var(--rule)}
  .contacts{list-style:none;font-size:15px;line-height:23px}
  .contacts li{display:flex;align-items:center;gap:8px}
  .contacts svg{width:11px;height:11px;fill:none;stroke:var(--red);stroke-width:2}
  .address{position:absolute;bottom:34px;left:0;right:0;text-align:center;font-size:15px}

  /* back */
  .back .brand{position:absolute;top:70px;left:40px}
  .back .brand-name{font-size:25px}
  .back .brand-tagline{font-size:15px;letter-spacing:2.6px}
  .services{position:absolute;right:34px;bottom:40px;text-align:center;font-size:16px;line-height:22px}
</style>
</head>
<body>
<main class="stage">
  <section class="card front" aria-label="Card front">
    <div class="brand">
      <div class="brand-row"><span class="brand-square"></span><span class="brand-name">Dara Whitmore, CPA, LLC</span></div>
      <div class="brand-tagline">Certified Public Accountant</div>
    </div>
    <div class="details">
      <div class="person">
        <div class="person-name">Dara Whitmore</div>
        <div class="person-title">Principal</div>
      </div>
      <div class="divider"></div>
      <ul class="contacts">
        <li><svg viewBox="0 0 12 12"><path d="M3 1 L5 4 L4 5 Q5 7 7 8 L8 7 L11 9 L10 11 Q4 11 1 3 Z"/></svg>555-014-2100</li>
        <li><svg viewBox="0 0 12 12"><rect x="1" y="2.5" width="10" height="7"/><path d="M1 2.5 L6 7 L11 2.5"/></svg>youremail@mailbox.com</li>
        <li><svg viewBox="0 0 12 12"><circle cx="6" cy="6" r="5"/><path d="M1 6 H11 M6 1 Q3 6 6 11 Q9 6 6 1"/></svg>www.yourwebsite.com</li>
      </ul>
    </div>
    <p class="address">Your address, city, state, ZIP 0000</p>
  </section>

  <section class="card back" aria-label="Card back">
    <div class="brand">
      <div class="brand-name">Dara Whitmore, CPA, LLC</div>
      <div class="brand-tagline">Certified Public Accountant</div>
    </div>
    <p class="services">Accounting<br>Tax &amp; Consulting Services</p>
  </section>
</main>
</body>
</html>
```